Byaruhanga & Odongo Advocates website

An interactive professional law firm website fully synchronized with social media pages.

Target Market(s)

Corporations and professionals

Industry/Entity Type

Professional Service

Number of Pages Required

5+ page

Font styles to use
Sans Serif

Colors

Designer to choose colors to be used in the design.

```html
<!DOCTYPE html>
<html lang="en">
<head>
<meta charset="utf-8">
<title>Byaruhanga &amp; Odongo Advocates</title>
<link href="https://fonts.googleapis.com/css2?family=Poppins:wght@400;500;600;700&family=Open+Sans:wght@400;600&display=swap" rel="stylesheet">
<style>
:root{
  --red:#9c1a2b;
  --red-dark:#7d1120;
  --ink:#1d1d1f;
  --grey:#5d5d62;
  --light:#f1f1f1;
  --dark:#26262a;
  --white:#ffffff;
}
*{box-sizing:border-box;margin:0;padding:0}
html,body{width:1200px;height:4775px;overflow:hidden}
body{font-family:"Open Sans",sans-serif;color:var(--ink);background:var(--white);font-size:13px;line-height:1.6}
h1,h2,h3,h4,.heading{font-family:"Poppins",sans-serif}
.wrap{width:940px;margin:0 auto;position:relative}
section,header,footer,nav{position:relative}

/* header */
.site-header{height:134px}
.site-header .wrap{display:flex;align-items:center;justify-content:space-between;height:134px}
.brand{display:flex;align-items:center;gap:12px}
.brand-square{width:46px;height:46px;background:var(--red)}
.brand-name{font-family:"Poppins",sans-serif;font-weight:600;color:var(--red);font-size:19px;line-height:1.15}
.brand-tag{font-size:9px;letter-spacing:2px;color:var(--grey);margin-top:6px;text-transform:uppercase}
.header-contact{display:flex;align-items:center;gap:12px;margin-left:150px}
.header-contact .phone{font-family:"Poppins",sans-serif;font-size:19px;font-weight:600;color:var(--red)}
.header-contact .mail{font-size:13px;color:var(--grey)}
.search{width:240px;height:34px;border:1px solid #ccc;border-radius:17px;display:flex;align-items:center;justify-content:space-between;padding:0 14px;color:#999;font-size:12px}

/* nav */
.main-nav{height:47px;background:var(--red)}
.main-nav ul{list-style:none;display:flex;justify-content:space-between;height:47px;align-items:center}
.main-nav li{color:var(--white);font-family:"Poppins",sans-serif;font-size:12.5px;font-weight:500;text-transform:uppercase}

/* hero */
.hero{height:532px;overflow:hidden}
.hero-photo{position:absolute;inset:0;background:linear-gradient(180deg,#6f7478 0%,#4a4f54 45%,#2c2f33 100%)}
.hero-content{position:absolute;inset:0;display:flex;flex-direction:column;align-items:center;justify-content:center;padding-top:20px}
.hero h1{color:var(--white);font-size:52px;font-weight:700;line-height:1.1;text-align:center;text-transform:uppercase;text-shadow:0 2px 8px rgba(0,0,0,.35)}
.btn-outline{margin-top:28px;border:2px solid var(--white);color:var(--white);border-radius:22px;padding:7px 26px;font-family:"Poppins",sans-serif;font-size:13px;font-weight:600;text-transform:uppercase}
.dots{display:flex;gap:8px;margin-top:24px}
.dots span{width:10px;height:10px;border-radius:50%;background:rgba(255,255,255,.5)}
.dots span:first-child{background:var(--white)}

/* welcome */
.welcome{height:522px}
.welcome .wrap{display:flex;justify-content:space-between;padding-top:95px}
.welcome-text{width:480px}
.welcome h2{font-size:30px;font-weight:600;line-height:1.25;text-transform:uppercase;margin-bottom:18px}
.welcome p{font-size:13px;color:var(--grey);margin-bottom:12px}
.btn-red{display:inline-block;background:var(--red);color:var(--white);font-family:"Poppins",sans-serif;font-size:12px;font-weight:600;padding:7px 20px;text-transform:uppercase;border-radius:3px}
.welcome-media{width:430px;height:320px;position:relative;margin-top:-5px}
.welcome-media .photo{position:absolute;inset:12px;background:linear-gradient(135deg,#8a7a6c,#3a2f2a)}
.corner{position:absolute;width:60px;height:60px;border:3px solid var(--red)}
.corner.tl{top:0;left:0;border-right:none;border-bottom:none}
.corner.tr{top:0;right:0;border-left:none;border-bottom:none}
.corner.bl{bottom:0;left:0;border-right:none;border-top:none}
.corner.br{bottom:0;right:0;border-left:none;border-top:none}
.play{position:absolute;left:50%;top:50%;transform:translate(-50%,-50%)}

/* who we are */
.who{height:541px;background:linear-gradient(180deg,#222226,#34343a);color:var(--white);text-align:center;padding-top:85px}
.section-title{font-size:40px;font-weight:700;text-transform:uppercase;letter-spacing:1px}
.who .lead{width:880px;margin:22px auto 0;font-size:13px;color:#dcdcdc}
.vm-cards{display:flex;justify-content:space-between;margin-top:38px}
.vm-card{width:448px;height:160px;background:var(--white);color:var(--ink);display:flex;align-items:center;gap:22px;padding:0 28px;text-align:left}
.vm-icon{width:92px;height:92px;border-radius:50%;background:var(--red);flex:none;display:flex;align-items:center;justify-content:center;box-shadow:0 0 0 6px #f1d4d8}
.vm-card h3{color:var(--red);font-size:17px;font-weight:700;text-transform:uppercase;margin-bottom:6px}
.vm-card p{font-size:12.5px;color:var(--grey)}

/* stats */
.stats{height:252px;background:linear-gradient(90deg,var(--red-dark),#b01d31);color:var(--white)}
.stats .wrap{display:flex;justify-content:space-between;height:252px;align-items:center}
.stat{width:235px;text-align:center;position:relative}
.stat + .stat::before{content:"";position:absolute;left:0;top:40px;height:100px;border-left:1px solid rgba(255,255,255,.45)}
.stat-icon{width:70px;height:70px;border-radius:50%;border:2px solid var(--white);margin:0 auto 14px;display:flex;align-items:center;justify-content:center}
.stat-num{font-family:"Poppins",sans-serif;font-size:24px;font-weight:700;line-height:1.2}
.stat-label{font-family:"Poppins",sans-serif;font-size:13px;font-weight:600;text-transform:uppercase;line-height:1.35}

/* how we do it */
.how{height:589px;text-align:center;padding-top:78px}
.how .section-title{color:var(--ink)}
.value-cards{display:flex;justify-content:space-between;margin-top:80px}
.value-card{width:290px;height:250px;border:2px solid var(--red);position:relative;padding:62px 22px 0}
.value-icon{position:absolute;top:-44px;left:50%;transform:translateX(-50%);width:88px;height:88px;border-radius:50%;background:var(--white);border:2px solid var(--red);display:flex;align-items:center;justify-content:center}
.value-card h3{font-size:17px;font-weight:700;text-transform:uppercase;margin-bottom:8px}
.value-card p{font-size:12px;color:var(--grey);line-height:1.55}
.pill{position:absolute;bottom:-11px;left:50%;transform:translateX(-50%);background:var(--white);border:2px solid var(--red);color:var(--red);border-radius:12px;font-family:"Poppins",sans-serif;font-size:10px;font-weight:600;padding:1px 14px;text-transform:uppercase}

/* practice */
.practice{height:646px;background:linear-gradient(180deg,#2c2c31,#1f1f23);text-align:center;padding-top:78px;color:var(--white)}
.practice-cards{display:flex;justify-content:space-between;margin-top:38px}
.practice-card{width:292px;height:360px;background:var(--white);color:var(--ink);position:relative;border-bottom:3px solid var(--red)}
.practice-card .photo{height:178px}
.practice-card h3{font-size:15px;font-weight:700;text-transform:uppercase;margin:16px 0 8px}
.practice-card p{font-size:12px;color:var(--grey);padding:0 22px;line-height:1.55}
.photo-a{background:linear-gradient(135deg,#c9cdd3,#7b8794)}
.photo-b{background:linear-gradient(135deg,#d8d3cb,#8f8474)}
.photo-c{background:linear-gradient(135deg,#6c6660,#2f2c2a)}

/* clients */
.clients{height:398px;padding-top:88px}
.tabs{display:flex;justify-content:center;gap:26px}
.tab{border:2px solid var(--red);color:var(--red);border-radius:20px;padding:6px 30px;font-family:"Poppins",sans-serif;font-size:13px;font-weight:500}
.tab.active{background:var(--red);color:var(--white)}
.client-row{display:flex;justify-content:space-between;margin-top:48px}
.client{width:122px;height:102px;border:1px solid #ddd;box-shadow:0 2px 6px rgba(0,0,0,.08);display:flex;align-items:center;justify-content:center;gap:6px;font-family:"Poppins",sans-serif;font-size:12px;font-weight:600;color:var(--grey)}
.client i{width:10px;height:10px;background:var(--red);display:block}

/* professionals */
.team{height:668px;background:linear-gradient(180deg,#a01d2e,var(--red-dark));color:var(--white);text-align:center;padding-top:110px;clip-path:polygon(0 60px,100% 0,100% 100%,0 100%)}
.team .lead{width:900px;margin:16px auto 0;font-size:13px;color:#f2d9dc}
.team-row{display:flex;justify-content:space-between;margin-top:70px}
.member{width:218px;height:300px;background:var(--white);color:var(--ink);position:relative;padding-top:100px}
.member .avatar{position:absolute;top:-48px;left:50%;transform:translateX(-50%);width:140px;height:140px;border-radius:50%;border:5px solid var(--white);background:linear-gradient(180deg,#8c7e74,#3b3431)}
.member h4{font-size:14px;font-weight:600;text-transform:uppercase;margin-top:12px}
.member .role{font-size:12px;color:var(--grey)}
.member p{font-size:11px;color:var(--grey);padding:6px 18px 0;line-height:1.5}
.socials{display:flex;justify-content:center;gap:8px;margin-top:10px}
.socials i{width:10px;height:10px;border-radius:50%;background:var(--red);display:block}
.arrow{position:absolute;top:310px}
.arrow.left{left:60px}.arrow.right{right:60px}

/* footer */
.site-footer{height:350px;background:var(--light);padding-top:70px}
.site-footer .wrap{display:flex;justify-content:space-between}
.site-footer h4{font-size:18px;font-weight:600;text-transform:uppercase;margin-bottom:22px}
.quick ul{list-style:none;font-size:12px;color:var(--grey);line-height:2}
.quick li::before{content:"› ";color:var(--red)}
.contact-list .row{display:flex;gap:12px;font-size:12px;color:var(--grey);margin-bottom:12px;align-items:flex-start}
.footer-brand{display:flex;align-items:center;gap:8px;margin-top:14px;font-family:"Poppins",sans-serif;font-weight:600;color:var(--red);font-size:15px}
.footer-brand i{width:26px;height:26px;background:var(--red);display:block}
.quick-form{width:440px}
.form-grid{display:grid;grid-template-columns:1fr 1fr;gap:12px}
.field{height:36px;background:var(--white);border:1px solid #ddd;font-size:11px;color:#999;padding:9px 12px}
.btn-submit{display:inline-block;margin-top:14px;background:var(--red-dark);color:var(--white);font-family:"Poppins",sans-serif;font-size:12px;font-weight:600;padding:8px 48px;text-transform:uppercase}

.bottom-bar{height:96px;border-top:1px solid #ddd}
.bottom-bar .wrap{display:flex;justify-content:space-between;align-items:center;height:96px;font-size:12px;color:var(--grey)}
.bottom-social{display:flex;gap:8px}
.bottom-social i{width:22px;height:22px;border-radius:50%;border:1.5px solid var(--red);display:block}
</style>
</head>
<body>

<header class="site-header">
  <div class="wrap">
    <div class="brand">
      <span class="brand-square"></span>
      <div>
        <div class="brand-name">Byaruhanga &amp; Odongo<br>Advocates</div>
        <div class="brand-tag">Construction Law | Arbitration | Litigation</div>
      </div>
    </div>
    <div class="header-contact">
      <svg width="24" height="24" viewBox="0 0 24 24"><path fill="#1d1d1f" d="M6.6 10.8a15 15 0 0 0 6.6 6.6l2.2-2.2c.3-.3.7-.4 1-.2 1.1.4 2.3.6 3.6.6.6 0 1 .4 1 1V20c0 .6-.4 1-1 1A17 17 0 0 1 3 4c0-.6.4-1 1-1h3.5c.6 0 1 .4 1 1 0 1.3.2 2.5.6 3.6.1.3 0 .7-.2 1z"/></svg>
      <div>
        <div class="phone">+256 (0) 41 7720 310</div>
        <div class="mail">info@byodongolaw.com</div>
      </div>
    </div>
    <div class="search">Search here
      <svg width="14" height="14" viewBox="0 0 24 24"><circle cx="10" cy="10" r="7" fill="none" stroke="#777" stroke-width="2.5"/><path d="M15 15l6 6" stroke="#777" stroke-width="2.5"/></svg>
    </div>
  </div>
</header>

<nav class="main-nav">
  <ul class="wrap">
    <li>Home</li><li>Our History</li><li>Who We Are</li><li>How We Do It</li><li>Practice Areas</li><li>Our Clients</li><li>Our Professionals</li><li>Contact Us</li>
  </ul>
</nav>

<section class="hero">
  <div class="hero-photo" role="img" aria-label="City skyline of office towers"></div>
  <div class="hero-content">
    <h1>Byaruhanga &amp; Odongo<br>Advocates</h1>
    <span class="btn-outline">Get More Info</span>
    <div class="dots"><span></span><span></span><span></span></div>
  </div>
</section>

<section class="welcome">
  <div class="wrap">
    <div class="welcome-text">
      <h2>Welcome to<br>Byaruhanga &amp; Odongo Advocates</h2>
      <p>In 1996, our firm was founded and is comprised of 5 Partners and over 15 Associates and support staff fully engaged and focused on client service. The firm is fully automated and is run on the latest practice management software with efficient client focused delivery systems and improved turn around times.</p>
      <p>Over the years, the firm has worked with the international firm of Harrowgate Lyle in successfully representing Civitas Rights Watch.</p>
      <span class="btn-red">Read More</span>
    </div>
    <div class="welcome-media">
      <div class="photo" role="img" aria-label="Lawyer reading case files at a desk"></div>
      <span class="corner tl"></span><span class="corner tr"></span><span class="corner bl"></span><span class="corner br"></span>
      <svg class="play" width="64" height="64" viewBox="0 0 64 64"><circle cx="32" cy="32" r="30" fill="#fff"/><path d="M26 20l18 12-18 12z" fill="#1d1d1f"/></svg>
    </div>
  </div>
</section>

<section class="who">
  <div class="wrap">
    <h2 class="section-title">Who We Are</h2>
    <p class="lead">Byaruhanga &amp; Odongo Advocates are a specialist commercial law firm in Uganda focusing on commercial litigation, construction law and arbitration. We have excelled in our niche areas for over two decades and we continue to grow and be the firm choice in those practice areas.</p>
    <div class="vm-cards">
      <div class="vm-card">
        <div class="vm-icon"><svg width="46" height="30" viewBox="0 0 46 30"><path d="M2 15C9 4 37 4 44 15 37 26 9 26 2 15z" fill="#fff"/><circle cx="23" cy="15" r="7" fill="#9c1a2b"/><circle cx="23" cy="15" r="3" fill="#fff"/></svg></div>
        <div><h3>Vision</h3><p>To be the firm of choice in our niche practice areas of commercial law, voluptatem accusantium doloremque.</p></div>
      </div>
      <div class="vm-card">
        <div class="vm-icon"><svg width="40" height="40" viewBox="0 0 40 40" fill="#fff"><rect x="4" y="14" width="14" height="24"/><rect x="20" y="4" width="16" height="34"/><g fill="#9c1a2b"><rect x="8" y="18" width="3" height="3"/><rect x="12" y="18" width="3" height="3"/><rect x="8" y="25" width="3" height="3"/><rect x="12" y="25" width="3" height="3"/><rect x="24" y="9" width="3" height="3"/><rect x="29" y="9" width="3" height="3"/><rect x="24" y="16" width="3" height="3"/><rect x="29" y="16" width="3" height="3"/><rect x="24" y="23" width="3" height="3"/><rect x="29" y="23" width="3" height="3"/></g></svg></div>
        <div><h3>Mission</h3><p>To provide legal services focused on commercial litigation, construction law and arbitration with efficiency, integrity and client satisfaction.</p></div>
      </div>
    </div>
  </div>
</section>

<section class="stats">
  <div class="wrap">
    <div class="stat"><div class="stat-icon"><svg width="30" height="30" viewBox="0 0 30 30" fill="#fff"><circle cx="15" cy="9" r="6"/><path d="M4 28c0-7 5-11 11-11s11 4 11 11z"/></svg></div><div class="stat-num">5</div><div class="stat-label">Partners</div></div>
    <div class="stat"><div class="stat-icon"><svg width="34" height="30" viewBox="0 0 34 30" fill="#fff"><circle cx="17" cy="8" r="5"/><circle cx="7" cy="11" r="4"/><circle cx="27" cy="11" r="4"/><path d="M8 28c0-6 4-10 9-10s9 4 9 10z"/><path d="M0 26c0-5 3-8 7-8 2 0 3 1 4 1-2 2-3 5-3 7z"/><path d="M34 26c0-5-3-8-7-8-2 0-3 1-4 1 2 2 3 5 3 7z"/></svg></div><div class="stat-num">20+</div><div class="stat-label">People</div></div>
    <div class="stat"><div class="stat-icon"><svg width="30" height="30" viewBox="0 0 30 30"><rect x="3" y="6" width="24" height="21" fill="none" stroke="#fff" stroke-width="2.5"/><path d="M3 12h24M9 3v6M21 3v6" stroke="#fff" stroke-width="2.5"/><g fill="#fff"><rect x="8" y="16" width="3" height="3"/><rect x="14" y="16" width="3" height="3"/><rect x="20" y="16" width="3" height="3"/><rect x="8" y="21" width="3" height="3"/><rect x="14" y="21" width="3" height="3"/></g></svg></div><div class="stat-num">55</div><div class="stat-label">Years of Combined<br>Experience</div></div>
    <div class="stat"><div class="stat-icon"><svg width="30" height="30" viewBox="0 0 30 30" fill="none" stroke="#fff" stroke-width="2.5"><path d="M3 3v24h24"/><path d="M7 22l6-7 5 4 8-10"/><path d="M21 9h5v5"/></svg></div><div class="stat-num">350+</div><div class="stat-label">Cases Solved</div></div>
  </div>
</section>

<section class="how">
  <div class="wrap">
    <h2 class="section-title">How We Do It</h2>
    <div class="value-cards">
      <div class="value-card">
        <div class="value-icon"><svg width="44" height="44" viewBox="0 0 44 44" fill="#9c1a2b"><circle cx="22" cy="8" r="5"/><circle cx="9" cy="32" r="5"/><circle cx="35" cy="32" r="5"/><path d="M22 14v8M22 22L11 27M22 22l11 5" stroke="#9c1a2b" stroke-width="2.5"/><path d="M2 44c0-4 3-6 7-6s7 2 7 6zM28 44c0-4 3-6 7-6s7 2 7 6z"/></svg></div>
        <h3>Integrity</h3>
        <p>We maintain ethical behaviour and strict moral values. We are honest and trustworthy in our dealings with each other, with our clients and with all others with whom we deal.</p>
        <span class="pill">Read More</span>
      </div>
      <div class="value-card">
        <div class="value-icon"><svg width="46" height="44" viewBox="0 0 46 44" fill="#9c1a2b"><circle cx="14" cy="7" r="5"/><circle cx="32" cy="7" r="5"/><path d="M6 24c0-6 3-10 8-10s8 4 8 10zM24 24c0-6 3-10 8-10s8 4 8 10z"/><rect x="4" y="26" width="38" height="5"/><path d="M10 31v12M36 31v12" stroke="#9c1a2b" stroke-width="3"/></svg></div>
        <h3>Partnership</h3>
        <p>We partner with our clients and keep a close and interactive relationship that enriches our business knowledge and allows us to provide strategic, innovative and forward-thinking solutions.</p>
        <span class="pill">Read More</span>
      </div>
      <div class="value-card">
        <div class="value-icon"><svg width="44" height="44" viewBox="0 0 44 44"><circle cx="20" cy="24" r="17" fill="none" stroke="#9c1a2b" stroke-width="3"/><circle cx="20" cy="24" r="10" fill="none" stroke="#9c1a2b" stroke-width="3"/><circle cx="20" cy="24" r="4" fill="#9c1a2b"/><path d="M20 24L40 4M34 4h6v6" stroke="#9c1a2b" stroke-width="3" fill="none"/></svg></div>
        <h3>Efficiency</h3>
        <p>We work to surpass our clients' expectations. We are practical and solution-driven in our approach. We are innovative and creative, and we focus sharply and firmly on the issues.</p>
        <span class="pill">Read More</span>
      </div>
    </div>
  </div>
</section>

<section class="practice">
  <div class="wrap">
    <h2 class="section-title">Practice Areas</h2>
    <div class="practice-cards">
      <div class="practice-card">
        <div class="photo photo-a" role="img" aria-label="Engineer in a hard hat reviewing building plans"></div>
        <h3>Construction Law</h3>
        <p>Our Construction Law department is headed by our Senior Partner Peter O. Odongo who is highly qualified and experienced in Construction law and</p>
        <span class="pill">Read More</span>
      </div>
      <div class="practice-card">
        <div class="photo photo-b" role="img" aria-label="Hand signing a legal document with a pen"></div>
        <h3>Commercial Litigation</h3>
        <p>We have a reputation for producing excellent results for our litigation clients. Since 1996, the firm has an excellent track record in winning for our clients in commercial</p>
        <span class="pill">Read More</span>
      </div>
      <div class="practice-card">
        <div class="photo photo-c" role="img" aria-label="Two professionals in discussion at a meeting table"></div>
        <h3>Arbitration</h3>
        <p>We advise clients on both domestic and international arbitration proceedings and other forms of intermediate and alternative dispute resolution, as well as on</p>
        <span class="pill">Read More</span>
      </div>
    </div>
  </div>
</section>

<section class="clients">
  <div class="wrap">
    <div class="tabs">
      <span class="tab active">Commercial Litigation &amp; Transactions</span>
      <span class="tab">Construction &amp; Arbitration</span>
      <span class="tab">Corporate Advisory</span>
    </div>
    <div class="client-row">
      <div class="client"><i></i>Swiftline</div>
      <div class="client"><i></i>Kobra Foods</div>
      <div class="client"><i></i>Nile Freight</div>
      <div class="client"><i></i>Acacia Group</div>
      <div class="client"><i></i>Packwell</div>
      <div class="client"><i></i>Lakeview</div>
      <div class="client"><i></i>Savanna Agro</div>
    </div>
  </div>
</section>

<section class="team">
  <div class="wrap">
    <h2 class="section-title">Our Professionals</h2>
    <p class="lead">Sed ut perspiciatis unde omnis iste natus error sit voluptatem accusantium doloremque laudantium, totam rem aperiam, eaque ipsa quae ab illo inventore veritatis et quasi architecto beatae vitae dicta sunt explicabo.</p>
    <div class="team-row">
      <div class="member"><div class="avatar" role="img" aria-label="Portrait of the managing partner"></div><h4>Samuel K. Byaruhanga</h4><div class="role">Managing Partner</div><p>Samuel K. Byaruhanga is currently the Managing Partner of the firm. He has over 28 years'</p><div class="socials"><i></i><i></i><i></i><i></i></div></div>
      <div class="member"><div class="avatar" role="img" aria-label="Portrait of the senior partner"></div><h4>Peter O. Odongo</h4><div class="role">Senior Partner</div><p>Peter is a Senior Partner at the firm with over 12 years experience in Construction law.</p><div class="socials"><i></i><i></i><i></i><i></i></div></div>
      <div class="member"><div class="avatar" role="img" aria-label="Portrait of a partner"></div><h4>Moses Atim</h4><div class="role">Partner</div><p>Moses is a Partner at the firm heading the Litigation Department. He started out his</p><div class="socials"><i></i><i></i><i></i><i></i></div></div>
      <div class="member"><div class="avatar" role="img" aria-label="Portrait of a partner"></div><h4>Grace Nakato</h4><div class="role">Partner</div><p>Grace is a Partner at the firm heading the Corporate Advisory team.</p><div class="socials"><i></i><i></i><i></i><i></i></div></div>
    </div>
  </div>
  <svg class="arrow left" width="24" height="44" viewBox="0 0 24 44"><path d="M22 2L2 22l20 20" fill="none" stroke="#fff" stroke-width="3"/></svg>
  <svg class="arrow right" width="24" height="44" viewBox="0 0 24 44"><path d="M2 2l20 20L2 42" fill="none" stroke="#fff" stroke-width="3"/></svg>
</section>

<footer class="site-footer">
  <div class="wrap">
    <div class="quick">
      <h4>Quick Link</h4>
      <ul><li>Home</li><li>Our History</li><li>Who We Are</li><li>How We Do It</li><li>Practice Areas</li><li>Our Clients</li><li>Our Professionals</li><li>Contact Us</li></ul>
    </div>
    <div class="contact-list">
      <h4>Contact Us</h4>
      <div class="row"><svg width="14" height="18" viewBox="0 0 14 18"><path d="M7 0a7 7 0 0 0-7 7c0 5 7 11 7 11s7-6 7-11a7 7 0 0 0-7-7z" fill="#9c1a2b"/><circle cx="7" cy="7" r="2.5" fill="#fff"/></svg><span>Plot 14, Kitante Road<br>2nd Floor, Crane House</span></div>
      <div class="row"><svg width="14" height="14" viewBox="0 0 24 24"><path fill="#9c1a2b" d="M6.6 10.8a15 15 0 0 0 6.6 6.6l2.2-2.2c.3-.3.7-.4 1-.2 1.1.4 2.3.6 3.6.6.6 0 1 .4 1 1V20c0 .6-.4 1-1 1A17 17 0 0 1 3 4c0-.6.4-1 1-1h3.5c.6 0 1 .4 1 1 0 1.3.2 2.5.6 3.6.1.3 0 .7-.2 1z"/></svg><span>Phone: 0414 550 218<br>+256 (0) 772 604 117</span></div>
      <div class="row"><svg width="14" height="12" viewBox="0 0 14 12"><rect width="14" height="12" fill="#9c1a2b"/><path d="M0 0l7 6 7-6" fill="none" stroke="#fff" stroke-width="1.5"/></svg><span>Email: advocates@byodongolaw.com</span></div>
      <div class="footer-brand"><i></i>Byaruhanga &amp; Odongo Advocates</div>
    </div>
    <div class="quick-form">
      <h4>Get a Quick Now!</h4>
      <div class="form-grid">
        <div class="field">Your Name</div><div class="field">Your E-Mail</div>
        <div class="field">Your Phone</div><div class="field">Message</div>
      </div>
      <span class="btn-submit">Submit</span>
    </div>
  </div>
</footer>

<div class="bottom-bar">
  <div class="wrap">
    <span>©2018 Byaruhanga &amp; Odongo Advocates. All Rights Reserved. Disclaimer | Privacy policy | Terms of use</span>
    <div class="bottom-social"><i></i><i></i><i></i><i></i></div>
  </div>
</div>

</body>
</html>
```